Fun Employee News and Engagement Portal - Brisk Oven Company

We are looking for a clean, but fun WordPress template for an internal employee engagement website. The site will be a place we share news, fun stories and pictures. We'll provide space for our employees to post comments, etc.
We are a deep dish pizza restaurant with a rich history. I'd love to see your take on a look and feel for us! The site will be called Tam-Zee. I've posted some images and colors along with this brief description.
Focus on making the template whimsical and fun! (Extra point for focusing on the "Lettering in lights" ).
I will continue to post additional pieces of art and content examples.
Reason: Our team is continuing to review designs. We've decided to extend the timing a few more days. Good luck! Make it playful!
Reason: We need more time with our team to review these designs. We are going to extend one more time!
Reason: Still trying to get enough time to review with the Tam-Zee team!
Reason: We are continuing to evaluate designs. Thank you!
Industry/Entity Type
American Restaurant
Number of Pages Required
1 page
Look and feel
Each slider illustrates characteristics of the customer's brand and the style your logo design should communicate.

```html
<!DOCTYPE html>
<html lang="en">
<head>
<meta charset="utf-8">
<title>Tam-Zee — Brisk Oven Company Employee Portal</title>
<link href="https://fonts.googleapis.com/css2?family=Open+Sans:wght@400;600;700&family=Patua+One&family=Bungee&display=swap" rel="stylesheet">
<style>
:root{
  --red:#e3262a;
  --red-deep:#c81d22;
  --yellow:#f8c94a;
  --gold:#ffd21f;
  --ink:#222;
  --grey:#666;
  --dark:#151212;
  --white:#fff;
  --footer-text:#c9c9c9;
}
*{box-sizing:border-box;margin:0;padding:0}
html,body{width:1200px;height:2929px;overflow:hidden}
body{position:relative;background:var(--white);font-family:"Open Sans",Arial,sans-serif;color:var(--ink)}
.abs{position:absolute}

/* top bar */
.topbar{left:0;top:0;width:1200px;height:30px;background:var(--red-deep);color:var(--white);font-size:11px;font-weight:600;z-index:3}
.topbar .contact{position:absolute;left:80px;top:8px;letter-spacing:.2px}
.topbar .contact span{margin-right:14px}
.topbar .login{position:absolute;right:80px;top:8px}
.dot-ico{display:inline-block;width:8px;height:8px;border-radius:50%;background:var(--gold);margin-right:5px;vertical-align:0}

/* hero */
.hero{left:0;top:0;width:1200px;height:620px;background:radial-gradient(ellipse at 60% 35%,#f0b24a 0%,#d8561f 35%,#a82a14 70%,#5a1a0e 100%)}
.brand{position:absolute;display:flex;align-items:center;gap:10px;color:var(--white);font-weight:700;font-size:34px;letter-spacing:.5px}
.brand .mark{width:46px;height:46px;border-radius:50%;background:var(--red)}
.hero .brand{left:210px;top:66px}
.nav{position:absolute;left:582px;top:66px;display:flex;gap:22px;font-size:13px;font-weight:700;color:var(--white);text-transform:uppercase}
.nav .active{color:var(--gold)}
.hero-title{position:absolute;left:0;width:1200px;top:210px;text-align:center;font-family:"Bungee",Impact,sans-serif;font-size:112px;color:#ff8a1e;letter-spacing:6px;text-shadow:0 0 14px #ffdc6a,0 0 3px #fff2b0}
.hero-sub{position:absolute;left:0;width:1200px;top:338px;text-align:center;color:var(--white);font-weight:700;font-size:15px;letter-spacing:2px;line-height:22px;text-transform:uppercase}
.slider-dots{position:absolute;left:582px;top:588px;display:flex;gap:6px}
.slider-dots i{width:9px;height:9px;border-radius:50%;border:2px solid var(--gold);display:block}
.slider-dots i.on{background:var(--gold)}
.hero-edge{left:0;top:500px}

/* section titles */
.section-title{position:absolute;left:0;width:1200px;text-align:center;font-family:"Patua One",Georgia,serif;font-variant:small-caps;font-size:58px;color:var(--red);letter-spacing:1px}
.section-title::after{content:"";display:block;width:180px;height:2px;background:var(--red);margin:4px auto 0}
.section-title.light{color:var(--white)}
.section-title.light::after{background:var(--white)}

/* news */
.news-arrows{left:1014px;top:765px;display:flex;gap:8px}
.news-arrows span{width:18px;height:18px;border-radius:50%;background:#ddd;display:flex;align-items:center;justify-content:center}
.news-arrows span.on{background:var(--red)}
.news-card{position:absolute;top:795px;width:272px;text-align:center}
.news-photo{width:272px;height:176px;border:4px solid #d8d8d8}
.news-card h3{margin-top:28px;font-size:23px;font-weight:700;color:var(--red-deep)}
.news-card p{margin:16px auto 0;width:262px;font-size:14px;line-height:22px;color:var(--grey)}
.btn{display:block;width:180px;height:44px;border:2px solid var(--red);color:var(--red);font-size:13px;font-weight:700;text-transform:uppercase;line-height:40px;text-align:center}
.news-card .btn{margin:28px auto 0}

/* employees */
.employees-bg{left:0;top:1270px}
.quote{position:absolute;left:0;width:1200px;top:1447px;text-align:center;color:var(--white);font-size:14px;line-height:22px}
.team{position:absolute;left:195px;top:1531px;display:flex;gap:15px}
.team i{display:block;width:66px;height:66px;border-radius:50%;border:3px solid var(--white);background:linear-gradient(160deg,#9a9a9a,#3a3a3a)}
.team i.current{border-color:var(--gold)}
.btn.ghost{border-color:var(--white);color:var(--white);left:510px;top:1655px;position:absolute}

/* about */
.about-text{position:absolute;left:228px;width:744px;top:2000px;text-align:center;font-size:14px;line-height:22px;color:var(--grey)}
.about-btn{position:absolute;left:510px;top:2153px}

/* footer */
.footer-bg{left:0;top:2260px}
.footer .brand{left:470px;top:2348px;font-size:44px}
.copyright{position:absolute;left:0;width:1200px;top:2440px;text-align:center;font-size:13px;color:#6d6d6d;letter-spacing:.5px}
.social{position:absolute;left:508px;top:2470px;display:flex;gap:48px}
.social i{display:block;width:12px;height:12px;border-radius:50%;background:#7a7a7a}
.footer-col{position:absolute;top:2566px;color:var(--footer-text);font-size:14px}
.footer-col h4{color:var(--red);font-size:14px;font-weight:700;text-transform:uppercase;letter-spacing:.5px}
.footer-col h4::after{content:"";display:block;width:62px;height:3px;background:var(--red);margin-top:10px}
.footer-col ul{list-style:none;margin-top:26px}
.footer-col li{height:33px;line-height:20px}
.footer-col li::before{content:"";display:inline-block;width:4px;height:4px;border-radius:50%;background:var(--red);margin-right:12px;vertical-align:3px}
.post{display:flex;gap:14px;margin-top:0;height:70px;width:250px;line-height:18px}
.post-list{margin-top:26px}
.post .avatar{flex:none;width:40px;height:40px;border-radius:50%;border:2px solid #ddd;background:linear-gradient(160deg,#8a8a8a,#333)}
.post b{display:block;color:#8a8a8a;font-weight:700}
</style>
</head>
<body>

<div class="abs topbar">
  <div class="contact"><span>&#9742; 1-800-555-0142</span><span>&#9993; info@tamzee-portal.com</span></div>
  <div class="login"><span class="dot-ico"></span>Employee Login</div>
</div>

<section class="abs hero" role="img" aria-label="Close-up photo of a deep dish pizza with peppers, olives and melted cheese">
  <div class="brand"><span class="mark"></span>Tam-Zee</div>
  <nav class="nav"><span class="active">Home</span><span>About us</span><span>Our team</span><span>Latest news</span><span>Gallery</span><span>Contacts</span></nav>
  <div class="hero-title">DEEP DISH</div>
  <div class="hero-sub">We are a deep dish pizza restaurant<br>with a rich history</div>
</section>
<svg class="abs hero-edge" width="1200" height="130" viewBox="0 0 1200 130">
  <path d="M0 120 Q700 130 1200 40 L1200 130 L0 130 Z" fill="var(--yellow)"/>
  <path d="M0 122 Q700 140 1200 62 L1200 130 L0 130 Z" fill="var(--white)"/>
</svg>
<div class="abs slider-dots"><i class="on"></i><i></i><i></i></div>

<h2 class="section-title" style="top:692px">Latest news</h2>
<div class="abs news-arrows">
  <span><svg width="8" height="8" viewBox="0 0 8 8"><path d="M5 1 L2 4 L5 7" stroke="#777" stroke-width="1.6" fill="none"/></svg></span>
  <span class="on"><svg width="8" height="8" viewBox="0 0 8 8"><path d="M3 1 L6 4 L3 7" stroke="#fff" stroke-width="1.6" fill="none"/></svg></span>
</div>

<article class="news-card" style="left:140px">
  <div class="news-photo" role="img" aria-label="Pizza slice topped with peppers and olives" style="background:linear-gradient(135deg,#2e2a20,#b8902a 45%,#6d2a18)"></div>
  <h3>Deep Dish Pizza</h3>
  <p>Sed ut perspiciatis unde omnis iste natus error sit voluptatem accusantium doloremque laudantium, totam rem...</p>
  <span class="btn">Read more</span>
</article>
<article class="news-card" style="left:464px">
  <div class="news-photo" role="img" aria-label="Hand lifting a cheesy pizza slice" style="background:linear-gradient(135deg,#d9692a,#f1c27a 50%,#b6401c)"></div>
  <h3>Deep Dish Pizza</h3>
  <p>Sed ut perspiciatis unde omnis iste natus error sit voluptatem accusantium doloremque laudantium, totam rem...</p>
  <span class="btn">Read more</span>
</article>
<article class="news-card" style="left:785px">
  <div class="news-photo" role="img" aria-label="Small dog in a party hat beside a birthday cake with candles" style="background:linear-gradient(135deg,#2a4a8a,#8a5a9a 50%,#d9a04a)"></div>
  <h3>Deep Dish Pizza</h3>
  <p>Sed ut perspiciatis unde omnis iste natus error sit voluptatem accusantium doloremque laudantium, totam rem...</p>
  <span class="btn">Read more</span>
</article>

<svg class="abs employees-bg" width="1200" height="500" viewBox="0 0 1200 500" role="img" aria-label="Red tinted pizza photo background">
  <defs><linearGradient id="redfill" x1="0" y1="0" x2="1" y2="1"><stop offset="0" stop-color="#e8302e"/><stop offset="1" stop-color="#d2201f"/></linearGradient></defs>
  <path d="M0 24 Q600 0 1200 20 L1200 370 Q600 520 0 370 Z" fill="url(#redfill)"/>
</svg>
<h2 class="section-title light" style="top:1365px">Our employees</h2>
<p class="quote">Design is not making beauty, beauty emerges from selection,<br>affinities, integration, love. - ELIAS MARROW</p>
<div class="team" aria-label="Employee portraits">
  <i class="current"></i><i></i><i></i><i></i><i></i><i></i><i></i><i></i><i></i><i></i>
</div>
<span class="btn ghost">See all our employees</span>

<h2 class="section-title" style="top:1888px">About us</h2>
<p class="about-text">Lorem ipsum dolor sit amet, consectetur adipiscing elit. Sed sollicitudin leo nibh, nec dignissim nibh sodales quis. Cras laoreet pharetra ipsum id posuere. Mauris nec eros quis ex eleifend ornare. Nulla eu aliquam sapien. Suspendisse venenatis, dui non congue porttitor, turpis arcu viverra risus, nec sodales lorem tellus in arcu. Mauris mollis massa non ligula dignissim blandit. Donec id massa ultrices, maximus turpis non, feugiat dolor. Nam eu est elementum, fringilla diam in, faucibus odio. Aliquam at dictum erat. Vivamus tristique cursus erat eu venenatis. Sed bibendum condimentum leo, non scelerisque ex ornare id.</p>
<span class="btn about-btn">Read more</span>

<svg class="abs footer-bg" width="1200" height="669" viewBox="0 0 1200 669" role="img" aria-label="Dark pizza photo background">
  <path d="M0 50 Q600 -10 1200 40 L1200 669 L0 669 Z" fill="var(--yellow)"/>
  <path d="M0 58 Q600 10 1200 80 L1200 669 L0 669 Z" fill="var(--dark)"/>
</svg>
<footer class="footer">
  <div class="brand"><span class="mark"></span>Tam-Zee</div>
  <div class="copyright">COPYRIGHT 2017. ALL RIGHTS RESERVED</div>
  <div class="social"><i></i><i></i><i></i><i></i></div>

  <div class="footer-col" style="left:146px">
    <h4>Quick link</h4>
    <ul><li>Home</li><li>About Us</li><li>Our Team</li><li>Latest News</li><li>Gallery</li><li>Contacts</li></ul>
  </div>
  <div class="footer-col" style="left:319px">
    <h4>Categories</h4>
    <ul><li>Lorem ipsum dolor.</li><li>Sit amet</li><li>Consectetur adipiscing elit.</li><li>Leo Nihb</li><li>Cras Laoreet</li><li>Sodales</li><li>Mauris nec</li></ul>
  </div>
  <div class="footer-col" style="left:549px">
    <h4>Recent posts</h4>
    <div class="post-list">
      <div class="post"><span class="avatar"></span><div>Lorem ipsum dolor sit amet, consectetur adipiscing elit.<b>February 28, 2017</b></div></div>
      <div class="post"><span class="avatar"></span><div>Leo nibh, nec dignissim nibh sodales quis.<b>February 24, 2017</b></div></div>
      <div class="post"><span class="avatar"></span><div>Cras laoreet pharetra ipsum id posuere. Mauris nec.<b>February 20, 2017</b></div></div>
    </div>
  </div>
  <div class="footer-col" style="left:842px">
    <h4>Recent comments</h4>
    <div class="post-list">
      <div class="post"><span class="avatar"></span><div>Lorem ipsum dolor sit amet, consectetur adipiscing elit.<b>Dana Oreti</b></div></div>
      <div class="post"><span class="avatar"></span><div>Leo nibh, nec dignissim nibh sodales quis.<b>Marco Velden</b></div></div>
      <div class="post"><span class="avatar"></span><div>Cras laoreet pharetra ipsum id posuere. Mauris nec.<b>Ilsa Brennick</b></div></div>
    </div>
  </div>
</footer>

</body>
</html>
```